Tessel PR (young, fun PR agency) needs a Business Card Design

We need a new business card design that reflects who we are as a company. We're a Sydney-based PR agency that's six years old with clients including Blue Heron, Duneprint, OLVEN, Lou Carvell etc. - just check out our website for more info: www.tesselpr.com.au. We would like to see designs that bring to life our company name and what we do (generating media coverage for brands on TV, radio, online and in newspapers and magazines). We don't want a corporate style card but one that people take notice of and think 'wow that's a cool business card'. It doesn't have to be the standard rectangle shape and can incorporate humour.

Target Market(s)

Clients (generally cool/creative types) and media

Industry/Entity Type

Business

Requirements
Must have
• The card must feature our business logo (which can be updated if you like) and use both sides.
Nice to have
• The card could feature a cool illustration

```html
<!DOCTYPE html>
<html lang="en">
<head>
<meta charset="utf-8">
<title>Tessel PR – Business Card</title>
<link rel="stylesheet" href="https://fonts.googleapis.com/css2?family=Luckiest+Guy&display=swap">
<style>
  :root {
    --page: #ffffff;
    --card: #000000;
    --ink: #ffffff;
    --cyan: #4fd3f5;
    --violet: #7b2fe8;
    --magenta: #f01ad2;
    --yellow: #fde51c;
    --lime: #49e81a;
    --brand: #e9e9e9;
  }
  html, body {
    margin: 0;
    padding: 0;
    width: 1036px;
    height: 1200px;
    overflow: hidden;
    background: var(--page);
  }
  .sheet {
    position: relative;
    width: 1036px;
    height: 1200px;
  }
  .card {
    position: absolute;
    left: 0;
    width: 1036px;
    background: var(--card);
    border-radius: 8px;
    overflow: hidden;
  }
  .card--front { top: 0; height: 595px; }
  .card--back { top: 604px; height: 596px; }

  .splat {
    position: absolute;
    border-radius: 46% 54% 50% 50% / 52% 46% 54% 48%;
  }
  .splat--cyan    { left: 22px;  top: 22px;  width: 260px; height: 400px;
                    background: radial-gradient(ellipse at 50% 35%, var(--cyan) 45%, rgba(79,211,245,0) 72%); }
  .splat--violet  { left: 255px; top: 30px;  width: 275px; height: 285px;
                    background: radial-gradient(circle at 50% 48%, var(--violet) 42%, rgba(123,47,232,0) 70%); }
  .splat--magenta { left: 478px; top: 145px; width: 250px; height: 230px;
                    background: radial-gradient(circle at 50% 50%, var(--magenta) 40%, rgba(240,26,210,0) 70%); }
  .splat--yellow  { left: 695px; top: 30px;  width: 330px; height: 330px;
                    background: radial-gradient(circle at 50% 48%, var(--yellow) 42%, rgba(253,229,28,0) 70%); }
  .splat--violet-back { left: 40px;  top: 230px; width: 285px; height: 285px;
                    background: radial-gradient(circle at 50% 50%, var(--violet) 42%, rgba(123,47,232,0) 70%); }
  .splat--yellow-back { left: 278px; top: 74px;  width: 420px; height: 415px;
                    background: radial-gradient(circle at 50% 48%, var(--yellow) 44%, rgba(253,229,28,0) 70%); }

  .brand {
    position: absolute;
    left: 345px;
    top: 398px;
    display: flex;
    align-items: center;
    gap: 26px;
  }
  .brand__name {
    font-family: "Luckiest Guy", "Impact", sans-serif;
    font-size: 82px;
    line-height: 1;
    color: var(--brand);
    letter-spacing: 2px;
  }
  .brand__mark {
    width: 150px;
    height: 150px;
  }

  .contact {
    position: absolute;
    left: 645px;
    top: 374px;
    font-family: "Luckiest Guy", "Impact", sans-serif;
    color: var(--ink);
    letter-spacing: 0.5px;
  }
  .contact__name {
    margin: 0 0 2px;
    font-size: 35px;
    line-height: 1.1;
    font-weight: 400;
  }
  .contact__line {
    margin: 0;
    font-size: 21px;
    line-height: 30px;
  }
</style>
</head>
<body>
<main class="sheet">
  <section class="card card--front" aria-label="Card front">
    <div class="splat splat--cyan" role="img" aria-label="Dripping cyan paint splat illustration"></div>
    <div class="splat splat--violet" role="img" aria-label="Purple paint splat illustration"></div>
    <div class="splat splat--magenta" role="img" aria-label="Magenta paint splat illustration"></div>
    <div class="splat splat--yellow" role="img" aria-label="Yellow paint splat illustration with green drips"></div>

    <div class="brand">
      <span class="brand__name">Tessel PR</span>
      <svg class="brand__mark" viewBox="0 0 150 150" aria-hidden="true">
        <circle cx="75" cy="75" r="70" fill="none" stroke="#ffffff" stroke-width="4"/>
      </svg>
    </div>
  </section>

  <section class="card card--back" aria-label="Card back">
    <div class="splat splat--violet-back" role="img" aria-label="Purple paint splat illustration"></div>
    <div class="splat splat--yellow-back" role="img" aria-label="Yellow paint splat illustration"></div>

    <div class="contact">
      <h1 class="contact__name">Renee Calloway</h1>
      <p class="contact__line">Managing Director</p>
      <p class="contact__line">Ph: 02 9000 1846</p>
      <p class="contact__line">renee@tesselpr.com.au</p>
      <p class="contact__line">Level 2, 18 Harlow Lane</p>
      <p class="contact__line">Surry Hills, Sydney 2010</p>
    </div>
  </section>
</main>
</body>
</html>
```